LARGE BANNER/SIGN DESIGN - RECRUITMENT/LABOUR HIRE COMPANY

We are a Labour Hire/Recruitment company from Australia. We will need to design some signs to be displayed on all of our building sites that we are involved in. We will be printing multiple signs (up to 50) to display all over Sydney.•

• Logo nice and big, taking up majority of the sign.
• “Linking Job Seekers with Employers” – maybe under the logo or to the side of it? Please see attached cover photo.
• I want a nice simple design that incorporates some graphic like the one attached (Maroon Boxes - you do not have to use these exact graphics, but something similar).
• We want to include “www.brightpathstaffing.com.au” and “1300 482 917” somewhere on the sign.
• Maintain the colour scheme of logo throughout the sign.
• If you would like to submit your own idea, go right ahead. As long as the logo is displayed, our website and the number.

The artwork needs to be 4000mm (W) x 2500mm (H), 150dpi and saved in PDF format. Creating this artwork in Adobe Illustrator is ideal.

I have included the logo in a PDF format. This will be printed on vinyl 450gsm material. It will be better if the background is white due to the colours of the logo but we can work with anything.

Submit your creative ideas. They do not have to have any specific graphics except for the logo. The logo needs to be exactly as provided. We will also need to display the website (www.brightpathstaffing.com.au) and our number (1300 482 917) on the sign.

Target Market(s)

Construction, builders, developers, general construction industry

Industry/Entity Type

Construction

Font styles to use
Sans Serif

Colors
ec1f27
474747

Requirements
Must have
• - Logo (as provided)
• - Website (www.brightpathstaffing.com.au)
• - Phone (1300 482 917)
• - This MUST be created in Adobe Illustrator and MUST be saved in PDF with resolution 4000mm (W) x 2500mm (H) with 150 DPI. A copy of the artwork in Illustrator MUST be provided on picking winner.
Nice to have
• Creative new ideas including the logo, website and phone. Anything at all! As long as colours are followed.

```html
<!DOCTYPE html>
<html lang="en">
<head>
<meta charset="utf-8">
<title>Bright Path – Site Sign</title>
<link rel="stylesheet" href="https://fonts.googleapis.com/css2?family=Outfit:wght@500;600;700&display=swap">
<style>
  :root {
    --page: #ffffff;
    --brand-red: #ec1f27;
    --stripe-red: #e00812;
    --brand-grey: #474747;
    --name-maroon: #8c1a1d;
    --sky-pink: #ee7a74;
    --ground-maroon: #3a2022;
    --panel-tint: rgba(110, 40, 40, 0.62);
    --text-light: #ffffff;
  }
  html, body {
    margin: 0;
    width: 1200px;
    height: 1051px;
    overflow: hidden;
    background: var(--page);
    font-family: "Outfit", sans-serif;
  }
  .site-sign {
    position: absolute;
    left: 161px;
    top: 226px;
    width: 877px;
    height: 548px;
    overflow: hidden;
  }
  .site-photo {
    position: absolute;
    inset: 0;
    background: linear-gradient(180deg, var(--sky-pink) 0%, #ec7d77 45%, #a2484a 68%, var(--ground-maroon) 100%);
  }
  .sign-bands {
    position: absolute;
    inset: 0;
  }
  .brand-name {
    position: absolute;
    left: 66px;
    top: 130px;
    margin: 0;
    display: flex;
    align-items: center;
    gap: 14px;
    font-size: 50px;
    font-weight: 700;
    letter-spacing: -1px;
    color: var(--name-maroon);
    line-height: 1;
  }
  .brand-mark {
    width: 30px;
    height: 30px;
    background: var(--brand-grey);
  }
  .contact {
    position: absolute;
    left: 470px;
    top: 118px;
    width: 392px;
    text-align: right;
    color: var(--text-light);
  }
  .contact-phone {
    display: block;
    font-size: 52px;
    font-weight: 600;
    line-height: 1;
    letter-spacing: -0.5px;
  }
  .contact-web {
    display: block;
    margin-top: 4px;
    font-size: 21px;
    font-weight: 600;
    letter-spacing: 0.3px;
  }
  .tagline {
    position: absolute;
    left: 0;
    right: 0;
    top: 306px;
    margin: 0;
    text-align: center;
    color: var(--text-light);
    font-size: 54px;
    font-weight: 600;
    line-height: 58px;
    letter-spacing: -0.3px;
    padding-right: 40px;
  }
</style>
</head>
<body>
  <section class="site-sign">
    <div class="site-photo" role="img" aria-label="Tower crane on a construction site against a red-tinted sky"></div>

    <svg class="sign-bands" width="877" height="548" viewBox="0 0 877 548" aria-hidden="true">
      <polygon points="464,83 877,83 877,232 414,232" fill="var(--panel-tint)"/>
      <polygon points="414,232 877,232 877,241 411,241" fill="rgba(255,210,205,0.55)"/>
      <polygon points="438,95 450,95 404,240 392,240" fill="rgba(255,190,185,0.55)"/>
      <polygon points="0,83 425,83 380,232 0,232" fill="var(--page)"/>
      <polygon points="425,95 437,95 386,241 374,241" fill="var(--stripe-red)"/>
      <polygon points="0,230 381,230 378,241 0,241" fill="var(--stripe-red)"/>
    </svg>

    <p class="brand-name"><span class="brand-mark"></span>bright path</p>

    <div class="contact">
      <span class="contact-phone">1300 482 917</span>
      <span class="contact-web">www.brightpathstaffing.com.au</span>
    </div>

    <h1 class="tagline">Linking Job Seekers<br>with Employers</h1>
  </section>
</body>
</html>
```